Bookmark Design

We would like to design a book mark with logos of our two business and a quote.

One side with the quote "The first wealth is health" - Tobias Quill Harrow and the two logos.

The back side has the two logos with its respective phone numbers and a common address (this is to be advised to the winner of the project).

```html
<!DOCTYPE html>
<html lang="en">
<head>
<meta charset="utf-8">
<title>Bookmark – Marrowdale Clinic &amp; Northgate Dental</title>
<link rel="stylesheet" href="https://fonts.googleapis.com/css2?family=Oswald:wght@300&family=Noto+Serif:wght@400&family=Roboto:wght@400;700&display=swap">
<style>
  :root{
    --stage:#33363d;
    --paper:#eef5fc;
    --brand-blue:#0e55a6;
    --brand-blue-deep:#0a4a96;
    --sky-light:#dbe9f7;
    --brand-green:#6cbf4b;
    --ink-dark:#1d3e6e;
    --white:#ffffff;
  }
  *{box-sizing:border-box;margin:0;padding:0}
  html,body{width:1200px;height:1177px;overflow:hidden;background:var(--stage)}
  .canvas{position:relative;width:1200px;height:1177px;font-family:"Roboto",Arial,sans-serif}

  /* Front side */
  .front{position:absolute;left:612px;top:26px;width:276px;height:833px;background:var(--paper);box-shadow:0 4px 14px rgba(0,0,0,.35)}
  .front__sky{position:absolute;left:13px;top:16px;width:250px;height:610px;border-radius:36px 36px 0 0;
    background:linear-gradient(180deg,var(--brand-blue) 0%,#3d7cc2 30%,#a9c9ea 58%,var(--sky-light) 78%,var(--paper) 100%)}
  .quote{position:absolute;left:0;top:76px;width:276px;text-align:center;color:var(--white)}
  .quote__lead{font-family:"Oswald",Arial,sans-serif;font-weight:300;font-size:43px;line-height:47px;letter-spacing:.5px}
  .quote__key{font-family:"Noto Serif",Georgia,serif;font-size:63px;line-height:74px;margin-top:4px}
  .quote__rule{width:218px;margin:2px auto 0;border-top:2px dotted rgba(255,255,255,.85)}
  .quote__author{font-size:21px;margin-top:10px}
  .front__scene{position:absolute;left:13px;top:416px;width:250px;height:210px;
    background:linear-gradient(180deg,rgba(238,245,252,0) 0%,rgba(238,245,252,.75) 55%,var(--paper) 100%)}

  .mark{display:flex;flex-direction:column;align-items:center;text-align:center;font-weight:700}
  .mark__dot{width:70px;height:70px;border-radius:50%;border:4px solid var(--brand-blue);margin-bottom:8px}
  .mark--clinic{color:var(--brand-blue-deep);font-size:21px;line-height:22px}
  .mark--dental{color:var(--brand-green);font-size:21px;line-height:22px}
  .front .mark--clinic{position:absolute;left:0;top:595px;width:276px}
  .front .mark--dental{position:absolute;left:0;top:750px;width:276px}

  /* Back side */
  .back{position:absolute;left:208px;top:874px;width:816px;height:271px;
    background:linear-gradient(90deg,var(--brand-blue-deep) 0%,var(--brand-blue) 35%,#5f95cf 60%,#c9dcf0 100%);
    box-shadow:0 4px 14px rgba(0,0,0,.35)}
  .back__frame{position:absolute;left:20px;top:18px;right:20px;bottom:18px;border:1.5px solid var(--brand-green);border-radius:24px}
  .back .mark--clinic{position:absolute;left:22px;top:72px;width:200px;color:var(--white)}
  .back .mark__dot{border-color:var(--white)}
  .contact{position:absolute;width:150px;text-align:center;color:var(--white);font-size:20px;line-height:26px}
  .contact--clinic{left:221px;top:40px}
  .contact__icon{display:block;margin:0 auto 6px;width:40px;height:40px}
  .contact__number{margin-bottom:14px;letter-spacing:1px}
  .back__panel{position:absolute;left:402px;top:30px;width:374px;height:210px;background:var(--paper);border-radius:32px}
  .back .mark--dental{position:absolute;left:14px;top:72px;width:180px}
  .contact--dental{left:198px;top:10px;color:#2a2f38}
</style>
</head>
<body>
<div class="canvas">

  <section class="front" aria-label="Bookmark front">
    <div class="front__sky"></div>
    <div class="quote">
      <p class="quote__lead">THE FIRST<br>WEALTH<br>IS</p>
      <p class="quote__key">Health</p>
      <div class="quote__rule"></div>
      <p class="quote__author">Tobias Quill Harrow</p>
    </div>
    <div class="front__scene" role="img" aria-label="Silhouette of a person with raised arms standing on a cliff above soft clouds"></div>
    <div class="mark mark--clinic"><span class="mark__dot"></span>MARROWDALE<br>CLINIC</div>
    <div class="mark mark--dental">NORTHGATE<br>DENTAL<br>MARROWDALE</div>
  </section>

  <section class="back" aria-label="Bookmark back">
    <div class="back__frame"></div>
    <div class="mark mark--clinic"><span class="mark__dot"></span>MARROWDALE<br>CLINIC</div>

    <div class="contact contact--clinic">
      <svg class="contact__icon" viewBox="0 0 40 40" aria-hidden="true"><circle cx="20" cy="20" r="18" fill="none" stroke="#fff" stroke-width="2"/><circle cx="20" cy="20" r="13" fill="#6cbf4b"/><path d="M15.5 13.5l2.5-.5 1.4 3.2-1.6 1.2a8 8 0 0 0 3.8 3.8l1.2-1.6 3.2 1.4-.5 2.5c-5.6.4-10.4-4.4-10-10z" fill="#fff"/></svg>
      <p class="contact__number">987654321</p>
      <svg class="contact__icon" viewBox="0 0 40 40" aria-hidden="true"><circle cx="20" cy="20" r="18" fill="none" stroke="#fff" stroke-width="2"/><circle cx="20" cy="20" r="13" fill="#6cbf4b"/><path d="M20 12a5 5 0 0 0-5 5c0 4 5 10 5 10s5-6 5-10a5 5 0 0 0-5-5zm0 7a2 2 0 1 1 0-4 2 2 0 0 1 0 4z" fill="#fff"/></svg>
      <p>Address 1<br>City ZIP Code</p>
    </div>

    <div class="back__panel">
      <div class="mark mark--dental">NORTHGATE<br>DENTAL<br>MARROWDALE</div>
      <div class="contact contact--dental">
        <svg class="contact__icon" viewBox="0 0 40 40" aria-hidden="true"><circle cx="20" cy="20" r="16" fill="#6cbf4b"/><path d="M14.5 12.5l2.8-.6 1.6 3.6-1.8 1.3a9 9 0 0 0 4.2 4.2l1.3-1.8 3.6 1.6-.6 2.8c-6.2.4-11.5-4.9-11.1-11.1z" fill="#fff"/></svg>
        <p class="contact__number">987654321</p>
        <svg class="contact__icon" viewBox="0 0 40 40" aria-hidden="true"><circle cx="20" cy="20" r="16" fill="#6cbf4b"/><path d="M20 11a5.5 5.5 0 0 0-5.5 5.5c0 4.4 5.5 11 5.5 11s5.5-6.6 5.5-11A5.5 5.5 0 0 0 20 11zm0 7.7a2.2 2.2 0 1 1 0-4.4 2.2 2.2 0 0 1 0 4.4z" fill="#fff"/></svg>
        <p>Address 1<br>City ZIP Code</p>
      </div>
    </div>
  </section>

</div>
</body>
</html>
```